Harbourline Wellness Collective Needs a Pro business Card

Hello Everyone,
Harbourline Wellness Collective needs a awesome, neat, professional business card design
Colours: follows the logo of Red(maroon) and dark Grey
About the company.
Harbourline Wellness Collective is a company which house a "group" of allied health professionals including Physiotherapy, and eventually podiatry , speech pathology, psychology etc.
I am a physiotherapist by trade, and this company will start off heading towards and establishing its physiotherapy division first. (including the physiotherapy practice, mobile physiotherapy service etc).
Details for the logo,
- Double sided
- You may have the Harbourline Physio on the front and the back with Harbourline wellness collective/ a holistic approach to healthcare" tag line
- i am going to leave the design to you.
My details
Name: Adrian Kestwell
Physiotherapist
B AppSc (Phty)
Phone: 0491625374
fax: 9186 4057
Address: PO Box 5172 Marlowe NSW 2094
Email: physio@harbourlinewellness.example.au
Web: www.harbourlinewellness.example.au

```html
<!DOCTYPE html>
<html lang="en">
<head>
<meta charset="utf-8">
<title>Harbourline Wellness Collective – Business Card</title>
<link rel="stylesheet" href="https://fonts.googleapis.com/css2?family=Crimson+Text:wght@400;700&display=swap">
<style>
  :root {
    --paper: #e4e1e1;
    --card: #555354;
    --ink: #f1efef;
    --ink-soft: #d9d6d6;
    --accent: #e0473a;
    --rule: #8d8a8b;
  }
  * { box-sizing: border-box; margin: 0; padding: 0; }
  html, body {
    width: 1200px; height: 1000px; overflow: hidden;
    background: var(--paper);
    font-family: "Crimson Text", Georgia, serif;
    color: var(--ink);
  }
  .sheet {
    width: 1200px; height: 1000px;
    display: flex; flex-direction: column;
    align-items: center; justify-content: center; gap: 56px;
  }
  .card {
    position: relative;
    width: 640px; height: 380px;
    background: var(--card);
    box-shadow: 0 6px 18px rgba(0,0,0,.18);
  }
  /* front */
  .card--front { display: flex; align-items: center; justify-content: center; }
  .brand { display: flex; align-items: center; gap: 12px; }
  .brand__square { width: 14px; height: 14px; background: var(--accent); flex: none; }
  .brand__name {
    font-size: 22px; letter-spacing: 1.5px; text-transform: uppercase;
    line-height: 1.05; color: var(--ink); font-weight: 400;
  }
  /* back */
  .back-brand {
    position: absolute; left: 34px; bottom: 52px;
    display: flex; align-items: center;
  }
  .back-brand .brand__name { font-size: 18px; letter-spacing: 1px; }
  .back-brand__rule { width: 1px; height: 44px; background: var(--rule); margin: 0 12px; }
  .tagline { font-size: 10px; line-height: 1.25; color: var(--ink-soft); }
  .details {
    position: absolute; right: 34px; top: 28px; text-align: right;
    color: var(--ink-soft); font-size: 15px; line-height: 1.25;
  }
  .person__name { font-size: 21px; font-weight: 700; color: var(--ink); }
  .person__surname { color: var(--accent); }
  .person__role { font-size: 16px; }
  .person__degree { font-size: 12px; }
  .details__address { margin-top: 22px; }
  .details__phones { margin-top: 10px; }
  .details__web { margin-top: 22px; }
  .label { font-weight: 700; color: var(--ink); }
  .sep { color: var(--accent); font-weight: 700; }
  .domain { font-weight: 700; color: var(--ink); }
</style>
</head>
<body>
<main class="sheet">
  <section class="card card--front" aria-label="Card front">
    <div class="brand">
      <span class="brand__square"></span>
      <span class="brand__name">Harbourline<br>Wellness Collective</span>
    </div>
  </section>

  <section class="card card--back" aria-label="Card back">
    <div class="details">
      <p class="person__name">Adrian <span class="person__surname">Kestwell</span></p>
      <p class="person__role">Physiotherapist</p>
      <p class="person__degree">B AppSc (Phty)</p>
      <p class="details__address">P.O. Box 5172 Marlowe NSW 2094</p>
      <div class="details__phones">
        <p><span class="label">T</span> <span class="sep">:</span> 0491625374</p>
        <p><span class="label">F</span> <span class="sep">:</span> 9186 4057</p>
      </div>
      <div class="details__web">
        <p><span class="label">E</span> <span class="sep">:</span> physio@harbourlinewellness.example.au</p>
        <p>www.<span class="domain">harbourlinewellness</span>.example.au</p>
      </div>
    </div>

    <div class="back-brand">
      <div class="brand">
        <span class="brand__square"></span>
        <span class="brand__name">Harbourline<br>Wellness Collective</span>
      </div>
      <span class="back-brand__rule"></span>
      <p class="tagline">A Holistic Approach<br>To Health Care</p>
    </div>
  </section>
</main>
</body>
</html>
```